2020-23 Strategic Plan - Graphic Design Work

We would would like to have our strategic plan designed. It should be two pages.

- I am looking for suggestions on ways to lay this out. I don’t like this boxy layout. It was great for the committee as we went through multiple versions, but I’d prefer the final not follow this boxy format

- I’ve included a few images we own (feel free to use any or none of them). Also attached our logo.

- Have a look at our new website to see our new branding look and feel (launching next week) https://thevorlex.plinthweb.com/

- I've included a copy of our logo.

Target Market(s)

Membership

Other font styles liked:
• Lato

Requirements
Must have
• Excellent layout. Easy to ready. Consistent with branding.

```html
<!DOCTYPE html>
<html lang="en">
<head>
<meta charset="utf-8">
<title>Vorlex 2020-2023 Strategic Plan</title>
<link rel="stylesheet" href="https://fonts.googleapis.com/css2?family=Lato:wght@400;700;900&display=swap">
<style>
:root{
  --green:#4e9a2c;
  --green-light:#8cc63f;
  --green-dark:#1d4f2a;
  --green-deep:#163f22;
  --grey-band:#e7e7e7;
  --grey-label:#a3a3a3;
  --grey-bg:#d9d9dd;
  --text:#1e1e1e;
  --white:#ffffff;
}
*{box-sizing:border-box;margin:0;padding:0}
html,body{width:1200px;height:1200px;overflow:hidden}
body{background:var(--grey-bg);font-family:"Lato",sans-serif;color:var(--text);position:relative}
.page{position:absolute;top:156px;width:540px;height:888px;background:var(--white);overflow:hidden;box-shadow:0 4px 14px rgba(0,0,0,.18)}
.page--cover{left:30px}
.page--pillars{left:630px}

/* brand name */
.brand{display:flex;align-items:center;gap:8px;font-weight:900;color:var(--green-dark);letter-spacing:.5px}
.brand__mark{width:22px;height:22px;background:var(--green)}
.brand__name{font-size:34px;line-height:1}
.brand__sub{font-size:8.5px;font-weight:700;color:var(--green-dark);letter-spacing:.6px;text-transform:uppercase;text-align:center;margin-top:3px}

/* cover page */
.cover-head{height:92px;display:flex;flex-direction:column;align-items:center;justify-content:center}
.cover-title{height:50px;background:var(--grey-band);display:flex;align-items:center;justify-content:center;font-size:31px;font-weight:900;color:var(--green-deep)}
.cover-title span{color:var(--green);margin-right:8px}
.cover-photo{position:relative;height:290px;background:linear-gradient(170deg,#3c3a6e 0%,#7a6290 30%,#b57a8d 45%,#334a6d 65%,#1d2a3c 100%)}
.cover-photo svg{position:absolute;left:0;bottom:0;width:540px;height:290px}
.intro{background:#f0f0f0;padding:18px 28px 16px;font-size:10px;line-height:1.35;text-align:justify;font-weight:700;height:105px}
.cover-body{position:relative;height:303px}
.statement{position:absolute;left:28px;width:228px;border:1.5px solid var(--green);padding:24px 14px 10px;font-size:9.6px;line-height:1.4;color:#333}
.statement--vision{top:30px;text-align:justify}
.statement--mission{top:148px}
.statement__tag{position:absolute;top:-12px;left:28px;width:170px;height:24px;background:var(--green-dark);color:var(--white);font-size:14px;display:flex;align-items:center;justify-content:center;letter-spacing:.3px}
.statement__tag b{margin-left:4px}
.values{position:absolute;left:296px;top:10px;width:236px;height:236px}
.values-note{position:absolute;left:282px;top:250px;width:245px;font-size:10px;font-weight:700;text-align:right;line-height:1.35}
.cover-foot{position:absolute;left:0;bottom:0;width:540px;height:58px}
.cover-foot__web{position:absolute;left:150px;top:0;width:240px;height:30px;background:var(--green-dark);clip-path:polygon(6% 0,94% 0,100% 100%,0 100%);color:var(--white);font-size:15px;font-weight:700;display:flex;align-items:center;justify-content:center;gap:6px;z-index:2}
.cover-foot__bar{position:absolute;left:0;bottom:0;width:100%;height:40px;background:var(--green);color:var(--white);font-size:10px;font-weight:700;display:flex;align-items:flex-end;justify-content:space-between;padding:0 20px 10px}
.contact-item{display:flex;align-items:center;gap:4px}
.contact-item svg{width:10px;height:10px;fill:var(--white)}

/* pillars page */
.pillars-title{height:40px;background:var(--green);color:var(--white);font-size:29px;text-align:center;line-height:42px;letter-spacing:.5px}
.pillar{height:195px;display:flex;flex-direction:column}
.pillar__head{height:38px;display:flex;background:var(--grey-band);position:relative}
.pillar__icon{width:86px;background:var(--green);display:flex;align-items:center;justify-content:center}
.pillar__icon svg{width:30px;height:30px}
.pillar__name{position:absolute;left:74px;top:4px;width:196px;height:30px;background:var(--green-dark);clip-path:polygon(6% 0,100% 0,92% 100%,0 100%);color:var(--white);font-size:21px;font-weight:700;padding-left:30px;line-height:31px}
.pillar__body{flex:1;background:var(--grey-band);padding:4px 8px 6px 0;display:flex;flex-direction:column}
.row{display:flex;flex:1}
.row__label{width:86px;background:var(--grey-label);color:var(--white);font-size:10px;font-weight:700;line-height:1;padding:8px 0 0 12px;text-transform:uppercase}
.row__text{flex:1;background:var(--white);padding:6px 10px;font-size:9px;line-height:1.3;border-bottom:1.5px dotted var(--green)}
.row:last-child .row__text{border-bottom:none;background:var(--grey-band)}
.row__text ul{list-style:none}
.row__text li{padding-left:8px;position:relative}
.row__text li::before{content:"";position:absolute;left:0;top:4px;width:4px;height:4px;border-radius:50%;background:var(--green)}
.row__text strong{font-weight:700}
.row__text .hl{color:var(--green)}
.row--objective .row__text{font-weight:700;display:flex;align-items:center}
.pillars-foot{position:absolute;left:0;bottom:0;width:540px;height:68px;display:flex}
.pillars-foot__brand{width:170px;background:var(--white);display:flex;flex-direction:column;justify-content:center;align-items:center}
.pillars-foot__brand .brand__name{font-size:26px}
.pillars-foot__info{flex:1;background:var(--green);position:relative;color:var(--white);font-size:10px;font-weight:700;padding:20px 10px 0 110px;display:grid;grid-template-columns:1fr auto;gap:2px 12px}
.pillars-foot__tag{position:absolute;left:0;top:0;width:96px;height:22px;background:var(--green-dark);clip-path:polygon(0 0,100% 0,92% 100%,0 100%);font-size:10.5px;display:flex;align-items:center;justify-content:center;letter-spacing:.4px}
</style>
</head>
<body>

<section class="page page--cover">
  <header class="cover-head">
    <div class="brand"><span class="brand__mark"></span><span class="brand__name">VORLEX</span></div>
    <div class="brand__sub">Institute of Property Valuers</div>
  </header>
  <h1 class="cover-title"><span>2020-2023</span> STRAGETIC PLAN</h1>
  <div class="cover-photo" role="img" aria-label="Upward view of glass city towers against a dusky sky">
    <svg viewBox="0 0 540 290" preserveAspectRatio="none" aria-hidden="true">
      <polygon points="0,175 540,175 540,240 270,290 0,240" fill="#4e9a2c" opacity=".78"/>
      <polygon points="0,240 270,290 540,240 540,290 0,290" fill="#f0f0f0"/>
    </svg>
  </div>
  <p class="intro">With over 1,250 members, the Vorlex Institute of Property Valuers is Canada's largest association of property assessment and taxation professionals. Our diverse membership is comprised of individuals from the private and public sectors practicing in the fields of assessment, consultancy, appraisal, taxation and law. Incorporated in May 1957, Vorlex is dedicated to advancing the interests, education and professional competence of its members. Our members are highly qualified and widely recognized as the leading professionals in the property assessment industry.</p>

  <div class="cover-body">
    <div class="statement statement--vision">
      <div class="statement__tag">OUR <b>VISION</b></div>
      To be the industry leader in education, ethical standards, and professional accreditation in the field of property assessment in Canada.
    </div>
    <div class="statement statement--mission">
      <div class="statement__tag">OUR <b>MISSION</b></div>
      To provide specialized education through a comprehensive approach to training which embraces all available technologies. To promote professional development and to ensure our members are recognized as experts in the field of property assessment and related functions.
    </div>

    <svg class="values" viewBox="-118 -118 236 236" role="img" aria-label="Values wheel">
      <g stroke="#ffffff" stroke-width="1.5">
        <path d="M-86,-68.6 A110,110 0 0 1 0,-110 L0,-58 A58,58 0 0 0 -45.3,-36.2Z" fill="#1e5b2c"/>
        <path d="M0,-110 A110,110 0 0 1 86,-68.6 L45.3,-36.2 A58,58 0 0 0 0,-58Z" fill="#13502a"/>
        <path d="M86,-68.6 A110,110 0 0 1 107.2,24.6 L56.5,13 A58,58 0 0 0 45.3,-36.2Z" fill="#1a6b4a"/>
        <path d="M107.2,24.6 A110,110 0 0 1 47.7,99.1 L25.2,52.3 A58,58 0 0 0 56.5,13Z" fill="#1f8a7a"/>
        <path d="M47.7,99.1 A110,110 0 0 1 -47.7,99.1 L-25.2,52.3 A58,58 0 0 0 25.2,52.3Z" fill="#7cb342"/>
        <path d="M-47.7,99.1 A110,110 0 0 1 -107.2,24.6 L-56.5,13 A58,58 0 0 0 -25.2,52.3Z" fill="#a5c93a"/>
        <path d="M-107.2,24.6 A110,110 0 0 1 -86,-68.6 L-45.3,-36.2 A58,58 0 0 0 -56.5,13Z" fill="#2f8c3f"/>
      </g>
      <circle r="54" fill="#e4e4e4"/>
      <circle r="46" fill="#ffffff"/>
      <g font-family="Lato, sans-serif" font-weight="700" font-size="7" fill="#ffffff" text-anchor="middle">
        <text x="-40" y="-66">ACCOUNTABILITY</text>
        <text x="38" y="-66">INTEGRITY</text>
        <text x="84" y="-14">DIVERSITY</text>
        <text x="66" y="58">ETHICS</text>
        <text x="0" y="94">PROFESSIONALISM</text>
        <text x="-66" y="58">INCLUSIVITY</text>
        <text x="-82" y="-14">EXPERTISE</text>
      </g>
      <text y="-2" text-anchor="middle" font-family="Lato, sans-serif" font-weight="900" font-size="17" fill="#1d4f2a">VORLEX</text>
      <text y="18" text-anchor="middle" font-family="Lato, sans-serif" font-weight="900" font-size="15" fill="#163f22">VALUES</text>
      <rect x="-30" y="22" width="60" height="2" fill="#c62828"/>
    </svg>
    <p class="values-note">Vorlex is committed to serving all members and stakeholders with competence and respect, rejecting all forms of prejudice and discrimination.</p>
  </div>

  <footer class="cover-foot">
    <div class="cover-foot__web">
      <svg width="12" height="12" viewBox="0 0 12 12" aria-hidden="true"><circle cx="6" cy="6" r="5" fill="none" stroke="#fff" stroke-width="1.2"/><ellipse cx="6" cy="6" rx="2.2" ry="5" fill="none" stroke="#fff"/><line x1="1" y1="6" x2="11" y2="6" stroke="#fff"/></svg>
      thevorlex.plinthweb.com
    </div>
    <div class="cover-foot__bar">
      <span class="contact-item"><svg viewBox="0 0 10 10"><path d="M5 0a3.5 3.5 0 0 0-3.5 3.5C1.5 6 5 10 5 10s3.5-4 3.5-6.5A3.5 3.5 0 0 0 5 0zm0 5a1.4 1.4 0 1 1 0-2.8A1.4 1.4 0 0 1 5 5z"/></svg>4410 Calder Avenue, Suite 12 Westbrook, Ontario L7B 2K4</span>
      <span class="contact-item"><svg viewBox="0 0 10 10"><path d="M2 0l2 2.5-1.2 1.3a6 6 0 0 0 3.4 3.4L7.5 6 10 8 8.6 9.6C4.5 10 0 5.5.4 1.4z"/></svg>905-555-0142</span>
      <span class="contact-item"><svg viewBox="0 0 10 10"><path d="M0 2h10v6H0zm1 1v.3l4 2.6 4-2.6V3zm0 1.4V7h8V4.4L5 7z"/></svg>info@vorlex.ca</span>
    </div>
  </footer>
</section>

<section class="page page--pillars">
  <h2 class="pillars-title">STRAGETIC <b>PILLAR</b></h2>

  <article class="pillar">
    <div class="pillar__head">
      <div class="pillar__icon"><svg viewBox="0 0 30 30" fill="none" stroke="#fff" stroke-width="1.6"><circle cx="15" cy="12" r="6"/><path d="M12 18v3h6v-3M13 24h4M15 2v2M6 6l1.5 1.5M24 6l-1.5 1.5M3 12h2M25 12h2"/></svg></div>
      <h3 class="pillar__name">EDUCATE</h3>
    </div>
    <div class="pillar__body">
      <div class="row row--objective"><div class="row__label">Strategic Objectives</div><div class="row__text">Be the most&nbsp;<span class="hl">TRUSTED, RELEVANT, and ACCESSIBLE</span>&nbsp;provider of education and credentials in the field of property assessment in Canada</div></div>
      <div class="row"><div class="row__label">Strategic Goals</div><div class="row__text"><ul><li>Ensure a catalogue of relevant, high-quality courses, which meet the evolving needs of assessment professionals</li><li>Provide an equal Vorlex member experience and service, regardless of geography</li></ul></div></div>
      <div class="row"><div class="row__label">Sample Supporting Actions</div><div class="row__text"><ul><li>Utilize technology to offer interactive and accessible online events</li><li>Develop provincial legislation-specific content for Vorlex courses</li><li>Lead opportunities for collaboration across districts to increase access to quality PD opportunities</li></ul></div></div>
    </div>
  </article>

  <article class="pillar">
    <div class="pillar__head">
      <div class="pillar__icon"><svg viewBox="0 0 30 30" fill="#fff"><path d="M15 26V14" stroke="#fff" stroke-width="2"/><path d="M14 15C6 15 4 9 4 5c6 0 11 3 10 10zM16 15c8 0 10-6 10-10-6 0-11 3-10 10z"/></svg></div>
      <h3 class="pillar__name">GROW</h3>
    </div>
    <div class="pillar__body">
      <div class="row row--objective"><div class="row__label">Strategic Objectives</div><div class="row__text">Increase Vorlex's membership by serving all career levels and forging strong strategic partnerships.</div></div>
      <div class="row"><div class="row__label">Strategic Goals</div><div class="row__text"><ul><li>Enhance opportunities for senior assessment professionals through the FVX designation.</li><li>Connect with young professionals by enhancing member communications, improving member onboarding, and expanding scholarship opportunities.</li></ul></div></div>
      <div class="row"><div class="row__label">Sample Supporting Actions</div><div class="row__text"><ul><li>Develop framework for a specialist designation track</li><li>Work collaboratively with strategic partners from across the country to develop criteria for, and launch, the FVX designation</li><li>Redesign the new member onboarding experience</li></ul></div></div>
    </div>
  </article>

  <article class="pillar">
    <div class="pillar__head">
      <div class="pillar__icon"><svg viewBox="0 0 30 30" fill="#fff"><circle cx="8" cy="9" r="3"/><circle cx="15" cy="6" r="3"/><circle cx="22" cy="9" r="3"/><rect x="5" y="13" width="6" height="12" rx="2"/><rect x="12" y="10" width="6" height="15" rx="2"/><rect x="19" y="13" width="6" height="12" rx="2"/></svg></div>
      <h3 class="pillar__name">LEAD</h3>
    </div>
    <div class="pillar__body">
      <div class="row row--objective"><div class="row__label">Strategic Objectives</div><div class="row__text">Strengthen the reputation of the organization and its members by acting as a leader within the field of property assessment in Canada</div></div>
      <div class="row"><div class="row__label">Strategic Goals</div><div class="row__text"><ul><li>Embrace the role of leader and advocate within the property assessment profession</li><li>Strengthen current, and develop new, strategic partnerships with peer associations across Canada.</li></ul></div></div>
      <div class="row"><div class="row__label">Sample Supporting Actions</div><div class="row__text"><ul><li>Embrace the role of leader and advocate within the property assessment profession</li><li>Adopt an advocacy voice for the assessment profession to ensure interests are being represented</li><li>Work with strategic partners to produce industry white papers with national relevance</li><li>Engage with various levels of government across Canada</li></ul></div></div>
    </div>
  </article>

  <article class="pillar">
    <div class="pillar__head">
      <div class="pillar__icon"><svg viewBox="0 0 30 30" fill="none" stroke="#fff" stroke-width="2"><path d="M15 3l10 4v7c0 7-5 11-10 13C10 25 5 21 5 14V7z"/><path d="M10 15l4 4 7-8"/></svg></div>
      <h3 class="pillar__name">GOVERN</h3>
    </div>
    <div class="pillar__body">
      <div class="row row--objective"><div class="row__label">Strategic Objectives</div><div class="row__text">Fortify the future of Vorlex through operational excellence &amp; a diverse group of talented volunteers</div></div>
      <div class="row"><div class="row__label">Strategic Goals</div><div class="row__text"><ul><li>Review and align association management practices with strategic objectives and statements of Vision, Mission and Values.</li><li>Secure Vorlex's financial stability by reviewing current pricing model and practicing sound risk management.</li></ul></div></div>
      <div class="row"><div class="row__label">Sample Supporting Actions</div><div class="row__text"><ul><li>Align the Vorlex budget and staffing needs to achieve clear strategic objectives</li><li>Utilize automation to modernize systems and administrative processes</li><li>Review and assess the relevance of current committees to determine if sufficient to meet the requirements of the strategic plan, and create new committees if deemed relevant</li></ul></div></div>
    </div>
  </article>

  <footer class="pillars-foot">
    <div class="pillars-foot__brand">
      <div class="brand"><span class="brand__mark" style="width:16px;height:16px"></span><span class="brand__name">VORLEX</span></div>
      <div class="brand__sub" style="font-size:7px">Institute of Property Valuers</div>
    </div>
    <div class="pillars-foot__info">
      <div class="pillars-foot__tag">CONTACT US</div>
      <span>4410 Calder Avenue, Suite 12<br>Westbrook, Ontario L7B 2K4</span>
      <span>905-555-0142<br>info@vorlex.ca</span>
      <span>thevorlex.plinthweb.com</span>
    </div>
  </footer>
</section>

</body>
</html>
```